EmberDepot, Charcoal bag packaging and brand

I'm looking at a package design for 10 KG/22 pounds of charcoal.
The design must include a name that is catchy and conveys quality, heat and low ash. The name must not violate any trademarks or tradenames. One of the best resources to view other packaging is the Quiet Pelican website. www.quietpelican.com
Two colors only and one must be red which will be printed on a kraft paper bag. The name EMBERDEPOT.COM must be prominent and also list our website of www.emberdepot.com.
Updates
Here is some wording for the front of the bag and it can be in any order. Make it look GREAT! Use the name "Blazewood Charcoal", but the Emberdepot logo should be the most prominant. Hi Heat, Low Ash, Long burning We will need some wording on the back and sides, but it's primarily just text and we won't worry about it until later. A UPC code will be necessary also. Thanks, Rick Tolben
100% Natural Hardwood Lump Charcoal
Restaurant and Competition grade
No additives, No fillers
Non sparking
Easy lighting, use a chimney starter
Mild flavor profile
A number of the designs are using full coverage ink.
Please limit the amount of ink coverage to no more than 25% ..
It becomes very costly to use 100% coverage.
Thanks!
Rick Tolben
Thank you to all the fine designers.
It was an extremely difficult decision for us. One fine designer was knocked out of the competition by our attorneys and we also received notice from the same attorneys that our brand of "Blazewood Charcoal" won't work...
I'll be posting another new logo design for branding of the charcoal at some point.
Kindest regards to all.
Rick Tolben
Target Market(s)
End users, restaurants, resorts, competition cookoffs
Look and feel
Each slider illustrates characteristics of the customer's brand and the style your logo design should communicate.

```html
<!DOCTYPE html>
<html lang="en">
<head>
<meta charset="utf-8">
<title>Ember Depot – Blazewood Charcoal Bag</title>
<link rel="stylesheet" href="https://fonts.googleapis.com/css2?family=Archivo+Black&family=Arimo:wght@700&display=swap">
<style>
  :root {
    --page: #ffffff;
    --kraft-light: #e2caa6;
    --kraft: #d8bd96;
    --red: #c8191b;
    --red-deep: #b8161a;
    --charcoal: #565656;
    --charcoal-dark: #4a4a4a;
    --white: #ffffff;
  }
  * { margin: 0; padding: 0; box-sizing: border-box; }
  html, body { width: 1200px; height: 900px; overflow: hidden; background: var(--page); }
  .canvas { position: relative; width: 1200px; height: 900px; }
  .bag {
    position: absolute; left: 292px; top: 0; width: 640px; height: 900px;
    background: radial-gradient(ellipse at 40% 35%, var(--kraft-light), var(--kraft));
    overflow: hidden;
    font-family: "Arimo", Arial, sans-serif;
    font-weight: 700;
  }
  .band { position: absolute; left: 0; width: 100%; background: linear-gradient(180deg, var(--red), var(--red-deep)); }
  .band--top { top: 24px; height: 70px; }
  .band--bottom { top: 693px; height: 207px; }
  .tagline {
    position: absolute; right: 27px; top: 44px;
    font-size: 24px; color: var(--charcoal); white-space: nowrap;
  }
  .burst { position: absolute; left: 0; top: 0; }
  .brand-name {
    position: absolute; left: 0; width: 640px; top: 168px; text-align: center;
    font-family: "Archivo Black", "Arial Black", sans-serif;
    font-size: 64px; line-height: 1; color: var(--white); letter-spacing: 1px;
  }
  .product-name {
    position: absolute; left: 0; width: 640px; top: 258px; text-align: center;
    font-size: 56px; line-height: 64px; color: var(--red);
  }
  .benefits { position: absolute; left: 160px; top: 528px; list-style: none; }
  .benefits li {
    display: flex; align-items: center; height: 40px;
    font-size: 32px; color: var(--red);
  }
  .benefits svg { width: 54px; height: 40px; margin-right: 18px; }
  .details {
    position: absolute; left: 35px; top: 718px; list-style: none;
    font-size: 19px; line-height: 25px; color: var(--charcoal);
  }
</style>
</head>
<body>
<div class="canvas">
  <div class="bag">
    <div class="band band--top"></div>
    <p class="tagline">100% Natural&nbsp; Hardwood Lump Charcoal</p>

    <svg class="burst" width="640" height="900" viewBox="0 0 640 900" aria-hidden="true">
      <defs>
        <polygon id="spike" points="-18.5,-186 0,-209 18.5,-186"/>
        <g id="star">
          <circle r="187"/>
          <use href="#spike" transform="rotate(0)"/><use href="#spike" transform="rotate(11.25)"/>
          <use href="#spike" transform="rotate(22.5)"/><use href="#spike" transform="rotate(33.75)"/>
          <use href="#spike" transform="rotate(45)"/><use href="#spike" transform="rotate(56.25)"/>
          <use href="#spike" transform="rotate(67.5)"/><use href="#spike" transform="rotate(78.75)"/>
          <use href="#spike" transform="rotate(90)"/><use href="#spike" transform="rotate(101.25)"/>
          <use href="#spike" transform="rotate(112.5)"/><use href="#spike" transform="rotate(123.75)"/>
          <use href="#spike" transform="rotate(135)"/><use href="#spike" transform="rotate(146.25)"/>
          <use href="#spike" transform="rotate(157.5)"/><use href="#spike" transform="rotate(168.75)"/>
          <use href="#spike" transform="rotate(180)"/><use href="#spike" transform="rotate(191.25)"/>
          <use href="#spike" transform="rotate(202.5)"/><use href="#spike" transform="rotate(213.75)"/>
          <use href="#spike" transform="rotate(225)"/><use href="#spike" transform="rotate(236.25)"/>
          <use href="#spike" transform="rotate(247.5)"/><use href="#spike" transform="rotate(258.75)"/>
          <use href="#spike" transform="rotate(270)"/><use href="#spike" transform="rotate(281.25)"/>
          <use href="#spike" transform="rotate(292.5)"/><use href="#spike" transform="rotate(303.75)"/>
          <use href="#spike" transform="rotate(315)"/><use href="#spike" transform="rotate(326.25)"/>
          <use href="#spike" transform="rotate(337.5)"/><use href="#spike" transform="rotate(348.75)"/>
        </g>
      </defs>
      <g transform="translate(317 326)">
        <use href="#star" fill="var(--charcoal-dark)"/>
        <use href="#star" fill="var(--kraft)" transform="scale(0.965)"/>
        <use href="#star" fill="var(--charcoal)" transform="scale(0.935)"/>
      </g>
    </svg>

    <h1 class="brand-name">Ember Depot</h1>
    <h2 class="product-name">Blazewood<br>Charcoal</h2>

    <ul class="benefits">
      <li><svg viewBox="0 0 54 40"><path d="M2 22 L12 16 L20 27 L46 2 L52 6 L21 38 Z" fill="var(--charcoal)"/></svg>High Heat</li>
      <li><svg viewBox="0 0 54 40"><path d="M2 22 L12 16 L20 27 L46 2 L52 6 L21 38 Z" fill="var(--charcoal)"/></svg>Low Ash</li>
      <li><svg viewBox="0 0 54 40"><path d="M2 22 L12 16 L20 27 L46 2 L52 6 L21 38 Z" fill="var(--charcoal)"/></svg>Long Burning</li>
    </ul>

    <div class="band band--bottom"></div>
    <ul class="details">
      <li>Restaurant and Competition grade</li>
      <li>No additives, No fillers</li>
      <li>Non sparking</li>
      <li>Easy lighting, use a chimney starter</li>
      <li>Mild flavor profile</li>
    </ul>
  </div>
</div>
</body>
</html>
```